web site update

I want to get a better website for a small high end remodeling and construction company
I currently have a web site but you will find that it is not good.
www.quenbrickhall.com
We are a high end construction / remodeling company that has been in business since 2003. We primarily work in the mid peninsula of the bay area. Most of our clientele are very educated captains of industry. This group is still the target client.
I had my logo designed by Mint Easel a few years ago and I do like it, I like the orange and black or orange a blue. I don’t have a lot of content on hand as far as professional photographs.
Number of pages not sure and are open to: design pages vs full function website
I think what I am after is a web presence that will seal the deal as we are getting high referrals from past clients.
Construction
1 page

```html
<!DOCTYPE html>
<html lang="en">
<head>
<meta charset="utf-8">
<title>Quenbrick Hall Remodeling</title>
<link href="https://fonts.googleapis.com/css2?family=Lato:wght@300;400;700;900&display=swap" rel="stylesheet">
<style>
:root{
  --orange:#f26a1b;
  --ink:#1c1c1c;
  --text:#8a8a8a;
  --soft:#9c9c9c;
  --line:#d6d6d6;
  --band:#f1f1f1;
  --white:#fff;
  --social:#2a5d99;
}
*{box-sizing:border-box;margin:0;padding:0}
html,body{width:759px;height:1200px;overflow:hidden;background:var(--white)}
body{position:relative;font-family:'Lato',sans-serif;color:var(--text);font-weight:300}
.abs{position:absolute}
.social-top{left:40px;top:45px;display:flex;gap:4px}
.social-top span{width:19px;height:19px;border-radius:50%;background:var(--social);display:block}
.brand{left:300px;top:32px;display:flex;align-items:center;gap:10px}
.brand-mark{width:44px;height:44px;background:var(--ink)}
.brand-name{color:var(--orange);font-weight:900;font-size:14px;line-height:15px;letter-spacing:.5px}
.search{left:562px;top:42px;width:158px;height:26px;border:1px solid var(--line);border-radius:4px}
.search svg{position:absolute;right:10px;top:7px}
.nav{left:152px;top:110px;display:flex;font-size:9.5px;color:#777;font-weight:400}
.nav a{display:block;height:31px;line-height:31px;padding:0 11px;color:inherit;text-decoration:none;margin-right:18px}
.nav a.active{border:1px solid var(--orange);color:var(--orange);border-radius:2px;margin-right:19px}
.hero{left:0;top:158px;width:759px;height:297px;background:linear-gradient(120deg,#6e6a63 0%,#a09a8f 35%,#5f564c 60%,#8a8275 100%)}
.hero-arrow{top:142px}
h2{position:absolute;width:759px;left:0;text-align:center;color:var(--orange);font-weight:400;font-size:13px;letter-spacing:.3px}
.welcome-text{left:110px;top:499px;width:539px;text-align:center;font-size:8.3px;line-height:14.5px}
.gallery{left:40px;top:585px;display:flex}
.gallery div{width:136px;height:112px}
.sub{left:0;top:750px;width:759px;text-align:center;font-size:10px;color:#b0b0b0}
.field{top:778px;height:22px;border:1px solid var(--line);border-radius:3px;font-size:10px;color:#b5b5b5;padding-left:12px;line-height:20px}
.submit{left:573px;top:778px;width:98px;height:22px;background:var(--orange);color:var(--white);font-size:10px;font-weight:400;text-align:center;line-height:22px;border-radius:2px}
.band{left:0;top:827px;width:759px;height:208px;background:var(--band)}
.card{top:873px;width:156px;height:146px;background:var(--white);border:1px solid var(--line);border-radius:2px;padding:12px 13px}
.card p{font-size:8.3px;line-height:14.3px}
.who{position:absolute;left:13px;top:92px;display:flex;gap:10px}
.avatar{width:47px;height:41px;border:1px solid var(--orange);border-radius:4px}
.who b{display:block;font-weight:400;color:#333;font-size:8.8px;margin-top:5px}
.who i{display:block;font-style:normal;font-size:8.5px;margin-top:4px}
.ft-title{top:1051px;color:var(--orange);font-size:10.5px;font-weight:400}
.links{left:41px;top:1076px;font-size:8.8px;line-height:16.6px;color:#666;list-style:none}
.contact{left:214px;top:1076px;font-size:8.8px;line-height:13px;color:#666}
.follow{left:214px;top:1150px;display:flex;gap:6px}
.follow span{width:19px;height:19px;border:1px solid #888;border-radius:50%;display:block}
.about{left:389px;top:1074px;width:330px;font-size:7.3px;line-height:13px;text-align:justify}
</style>
</head>
<body>
<div class="abs social-top"><span></span><span></span><span></span></div>
<div class="abs brand"><div class="brand-mark"></div><div class="brand-name">QUENBRICK<br>HALL<br>REMODELING</div></div>
<div class="abs search"><svg width="10" height="10" viewBox="0 0 10 10"><circle cx="4" cy="4" r="3" fill="none" stroke="#f26a1b" stroke-width="1.5"/><line x1="6.2" y1="6.2" x2="9" y2="9" stroke="#f26a1b" stroke-width="1.5"/></svg></div>
<nav class="abs nav"><a class="active">HOME</a><a>ABOUT US</a><a>SERVICES</a><a>GALLERY</a><a>PRICING</a><a>CONTACT</a></nav>
<div class="abs hero" role="img" aria-label="Sunlit room with an armchair beside large windows">
  <svg class="abs hero-arrow" style="left:38px" width="14" height="26"><polyline points="12,2 2,13 12,24" fill="none" stroke="#777" stroke-width="1.5"/></svg>
  <svg class="abs hero-arrow" style="left:706px" width="14" height="26"><polyline points="2,2 12,13 2,24" fill="none" stroke="#999" stroke-width="1.5"/></svg>
</div>
<h2 style="top:476px">WELCOME</h2>
<p class="abs welcome-text">Eos et accumsan et iusto odio dignissim qui blandit praesent luptatum zzelenit augue duis dolore te feugait nulla facilisi. Typi non habent claritatem insita. Claritas est etiam processus dynamicusqui sequitur mutationem consuetudium lectorum. Mirum est notare quam littera gothica, quam nuEodemo ui blandit praesent luptatum zzelenit augue.</p>
<h2 style="top:563px">GALLERY</h2>
<div class="abs gallery">
  <div role="img" aria-label="Living room with fireplace" style="background:linear-gradient(#c9c3b5,#5a4a3a)"></div>
  <div role="img" aria-label="Kitchen with wooden cabinets and range" style="background:linear-gradient(#a8663a,#d8c7aa)"></div>
  <div role="img" aria-label="Modern kitchen with dark cabinets" style="background:linear-gradient(#e2e2e2,#3a2e28)"></div>
  <div role="img" aria-label="White kitchen with steel fridge" style="background:linear-gradient(#d9d2c8,#8a7d70)"></div>
  <div role="img" aria-label="Kitchen island with granite top" style="background:linear-gradient(#e8e4de,#8a7a60)"></div>
</div>
<h2 style="top:730px">SIGN UP BELOW TO GET NEWS &amp; DEALS!</h2>
<p class="abs sub">Subscribe to Mailling List</p>
<div class="abs field" style="left:70px;width:242px">Your Name</div>
<div class="abs field" style="left:321px;width:242px">Your E-mail</div>
<div class="abs submit">Submit</div>
<div class="abs band"></div>
<h2 style="top:843px">TESTIMONIALS</h2>
<div class="abs card" style="left:40px"><p>Forget carrying your clothes to the dry cleaner or washing them at home. Just go to FreshFold.co and select your pickup and delivery times. It is that...</p><div class="who"><div class="avatar" role="img" aria-label="Client portrait" style="background:#b9a088"></div><div><b>Daniel Corwin</b><i>London</i></div></div></div>
<div class="abs card" style="left:214px"><p>No maid! no washing machine!! Only one website... FreshFold will soon be one of my favorite start ups Great work guys... My best wishes with you!!</p><div class="who"><div class="avatar" role="img" aria-label="Client portrait" style="background:#6f6e70"></div><div><b>Robert Ashby</b><i>London</i></div></div></div>
<div class="abs card" style="left:389px"><p>Forget carrying your clothes to the dry cleaner or washing them at home. Just go to FreshFold.co and select your pickup and delivery times. It is that...</p><div class="who"><div class="avatar" role="img" aria-label="Client portrait" style="background:#5a4038"></div><div><b>Clarissa Kent</b><i>London</i></div></div></div>
<div class="abs card" style="left:563px"><p>No maid! no washing machine!! Only one website... FreshFold will soon be one of my favorite start ups Great work guys... My best wishes with you!!</p><div class="who"><div class="avatar" role="img" aria-label="Client portrait" style="background:#2f5f8f"></div><div><b>colin marsh</b><i>London</i></div></div></div>
<div class="abs ft-title" style="left:40px">QUICK LINKS</div>
<ul class="abs links"><li>Home</li><li>About Us</li><li>Services</li><li>Blog</li><li>Pricing</li><li>Contact</li></ul>
<div class="abs ft-title" style="left:214px">CONTACT US</div>
<div class="abs contact">
  <div style="display:flex;gap:6px"><svg width="6" height="9" viewBox="0 0 6 9"><path d="M3 0a3 3 0 0 1 3 3c0 2-3 6-3 6S0 5 0 3a3 3 0 0 1 3-3z" fill="#666"/></svg><span>4120 Elmstead Road,<br>Halford, H12 7QP</span></div>
  <div style="display:flex;gap:6px;margin-top:5px;align-items:center"><svg width="8" height="8" viewBox="0 0 8 8"><path d="M1 0l2 2-1 1c.5 1.2 1.8 2.5 3 3l1-1 2 2-1.5 1C3 8 0 5 0 1.5z" fill="#666"/></svg><span>(555) 014-2290</span></div>
</div>
<div class="abs ft-title" style="left:214px;top:1132px">FOLLOW US</div>
<div class="abs follow"><span></span><span></span><span></span></div>
<div class="abs ft-title" style="left:388px">QUENBRICKHALL</div>
<p class="abs about">Lorem Ipsum is simply dummy text rinting and typesetting industry. Lorem Ipsum has been the industry's standard dummy text ever since the 1500s, when an unknown printer took a galley of type and scrambled it to make a type specimen book. It has survived not only five centuries, but also the leap into electronic Lorem Ipsum is simply dummy text rinting and typesetting industry. Lorem Ipsum has been the industry's standard dummy text ever since the 1500s, when an unknown printer took a galley of type and scrambled it to make a type specimen book. It has survived not only five centuries, but also the leap into electronic Lorem Ipsum is simply dummy</p>
</body>
</html>
```